Pilates 1 on 1 Session

A double sided DL size flyer.

Features

- Harbor Motion Clinic Logo (see EPS)
- Pictures only from our photo stock (no random downloaded images).
- Text relevant to the offer we are making (see DL Text file)
- Phone Number and Email Address
- Include photos see URL www.harbormotionclinic.com.au and those already attached.
- Please incorporate the pilates_studio image file attached as well.

This flyer is designed to bring people in for a 1v1 pilates session with our senior physio. Those who have health insurance will not need to pay anything out of pocket as it is completely covered. After the this session they will then be able to join any one of the other 17 Small pilates groups that we run (by small we mean max of 5 people).

Prefer cool colours like the greens from our logo and perhaps some blue as well.

Cheers

Target Market(s)

Females 20 through to 60 who are interested in fitness and personal health.

Industry/Entity Type

Health

Font styles to use
Sans Serif

Colors
acd036
9bcb3c
0255a3

Requirements
Must have
• Images of pilates equipment that were provided.
Should not have
• Any pictures that have not been supplied either as part of this job or on the website.

```html
<!DOCTYPE html>
<html lang="en">
<head>
<meta charset="utf-8">
<title>Harbor Motion Clinic – Pilates 1 on 1 Session</title>
<link href="https://fonts.googleapis.com/css2?family=Fredoka:wght@600&family=Source+Sans+3:wght@600;700&display=swap" rel="stylesheet">
<style>
  :root {
    --brand-blue: #0255a3;
    --brand-green: #9bcb3c;
    --brand-lime: #acd036;
    --paper: #ffffff;
    --studio-dark: #3a3a3a;
    --studio-light: #d9d9d9;
  }
  html, body { margin: 0; padding: 0; overflow: hidden; }
  body { width: 923px; height: 1200px; background: var(--paper); }
  .flyer {
    position: relative;
    width: 923px;
    height: 1200px;
    overflow: hidden;
    background: var(--paper);
    font-family: "Source Sans 3", Arial, sans-serif;
  }
  .top-bar {
    position: absolute; left: 0; top: 0; width: 605px; height: 52px;
    background: var(--brand-lime);
  }
  .top-rule {
    position: absolute; left: 0; top: 54px; width: 605px; height: 8px;
    background: var(--brand-blue);
  }
  .info-column {
    position: absolute; left: 605px; top: 0; width: 318px; height: 800px;
    background: var(--brand-blue);
  }
  .brand {
    position: absolute; left: 92px; top: 110px;
    display: flex; align-items: center; gap: 14px;
    font-family: "Source Sans 3", Arial, sans-serif;
    font-weight: 700; font-size: 38px; line-height: 1;
    color: var(--brand-green);
  }
  .brand-dot {
    width: 26px; height: 26px; border-radius: 50%;
    background: var(--brand-green);
  }
  .headline {
    position: absolute; left: 89px; top: 262px; width: 500px; margin: 0;
    font-family: "Fredoka", "Arial Rounded MT Bold", sans-serif;
    font-weight: 600; font-size: 55px; line-height: 54px;
    color: var(--brand-blue);
  }
  .offer {
    position: absolute; left: 89px; top: 492px; width: 480px; margin: 0;
    font-weight: 700; font-size: 26px; line-height: 33px;
    color: var(--brand-green);
  }
  .session-note {
    position: absolute; left: 89px; top: 622px; width: 420px; margin: 0;
    font-weight: 700; font-size: 26px; line-height: 33px;
    color: var(--brand-blue);
  }
  .column-text {
    position: absolute; right: 34px; margin: 0; text-align: right;
    font-weight: 700; font-size: 21px; line-height: 27px;
    color: var(--paper);
  }
  .promise { top: 77px; width: 240px; }
  .session-type { top: 276px; }
  .coverage-band {
    position: absolute; left: 581px; top: 341px; width: 342px; height: 77px;
    background: var(--brand-green);
    display: flex; flex-direction: column; justify-content: center; align-items: center;
    font-weight: 700; font-size: 20px; line-height: 25px; text-align: center;
    color: var(--paper);
  }
  .contact { top: 664px; font-size: 23px; line-height: 30px; }
  .bottom-band {
    position: absolute; left: 0; top: 800px; width: 923px; height: 20px;
    background: var(--brand-lime);
  }
  .studio-photo {
    position: absolute; left: 0; top: 820px; width: 923px; height: 380px;
    background: linear-gradient(180deg, var(--studio-light) 0%, #bdbdbd 45%, var(--studio-dark) 100%);
  }
</style>
</head>
<body>
<main class="flyer">
  <div class="top-bar"></div>
  <div class="top-rule"></div>
  <aside class="info-column"></aside>

  <div class="brand"><span class="brand-dot"></span><span>Harbor Motion Clinic</span></div>

  <h1 class="headline">Have you ever wondered about trying Pilates?</h1>

  <p class="offer">Experience a one hour session with a principle physio who has 25 years of experience and it will be recovered 100% by your health insurance.</p>

  <p class="session-note">Session lasts an hour and includes a complete physiotherapy assessment.</p>

  <p class="column-text promise">Professional therapists that work with you and your doctor to achieve real results.</p>

  <p class="column-text session-type">One Hour private<br>one-on-one Pilates session</p>

  <div class="coverage-band"><span>COVERED 100% BY YOUR</span><span>PRIVATE HEALTH INSURANCE</span></div>

  <p class="column-text contact">Phone: (08) 7155 0342<br>harbormotionclinic.com.au</p>

  <div class="bottom-band"></div>
  <div class="studio-photo" role="img" aria-label="Photo of the clinic's Pilates studio with reformer machines, trapeze table, arc barrel and exercise balls"></div>
</main>
</body>
</html>
```